Halvern Aviation Group - "Coming Soon" Main Company Webpage

Design a main webpage that can be posted while a fully functional website is constructed. The design should be created to convey a sense of luxury and exclusivity. The main page should contain only one photo as the background. The photo I believe to show "luxury" and "Exclusivity" is listed as "Global Luxury Photo". I have included two other photos as well to aid in providing a variety of presentations.
The "Member PQTR" logo should appear somewhere on the main page but be less prevalent than the main company logo. "Coming Soon" should also appear to convey that a website is being constructed.
Tabs for the website:
- Aircraft Management
- Aircraft Sales
- Pilot Services
- Charter
- Flight Training

```html
<!DOCTYPE html>
<html lang="en">
<head>
<meta charset="utf-8">
<title>Halvern Aviation Group — Coming Soon</title>
<link href="https://fonts.googleapis.com/css2?family=Cormorant+Garamond:wght@400;500&family=Manrope:wght@400;500&display=swap" rel="stylesheet">
<style>
  :root {
    --ink: #2e2e2e;
    --stone: #9a9895;
    --silver: #b9b8ba;
    --mist: #dfdfe1;
    --canvas: #efefef;
    --nav: #6b6a68;
    --tile: rgba(255, 255, 255, 0.55);
  }
  * { box-sizing: border-box; margin: 0; padding: 0; }
  html, body {
    width: 897px;
    height: 1200px;
    overflow: hidden;
    background: var(--canvas);
    font-family: "Manrope", sans-serif;
    color: var(--ink);
  }
  .page {
    position: absolute;
    left: 0;
    top: 320px;
    width: 897px;
    height: 560px;
    overflow: hidden;
  }
  .hero-photo {
    position: absolute;
    inset: 0;
    background:
      linear-gradient(100deg, rgba(236,236,236,0) 0%, rgba(236,236,236,0) 62%, rgba(244,244,244,0.9) 82%, #f1f1f1 100%),
      linear-gradient(180deg, #ededed 0%, #dedede 45%, #cbcbcb 100%);
  }
  .site-header {
    position: absolute;
    top: 16px;
    left: 120px;
    right: 120px;
    display: flex;
    align-items: center;
    justify-content: space-between;
  }
  .brand {
    font-family: "Manrope", sans-serif;
    font-weight: 500;
    font-size: 9px;
    line-height: 1.1;
    letter-spacing: 0.12em;
    text-transform: uppercase;
    color: var(--stone);
  }
  .brand-name { font-size: 11px; letter-spacing: 0.14em; }
  .main-nav {
    display: flex;
    align-items: center;
    gap: 27px;
    font-size: 7px;
    color: var(--nav);
  }
  .menu-icon { display: block; }
  .hero-content {
    position: absolute;
    left: 120px;
    top: 203px;
  }
  .kicker {
    font-family: "Cormorant Garamond", serif;
    font-weight: 500;
    font-size: 8px;
    letter-spacing: 0.5em;
    text-transform: uppercase;
    color: var(--ink);
    white-space: nowrap;
  }
  .headline {
    font-family: "Cormorant Garamond", serif;
    font-weight: 400;
    font-size: 63px;
    line-height: 0.9;
    letter-spacing: -0.035em;
    text-transform: uppercase;
    color: var(--ink);
    margin-top: 5px;
    white-space: nowrap;
  }
  .launch-label {
    font-size: 7px;
    color: var(--nav);
    margin-top: 24px;
  }
  .countdown {
    display: flex;
    gap: 9px;
    margin-top: 7px;
  }
  .countdown-tile {
    width: 53px;
    height: 53px;
    background: var(--tile);
    display: flex;
    align-items: center;
    justify-content: center;
    font-family: "Cormorant Garamond", serif;
    font-variant-numeric: lining-nums;
    font-size: 16px;
    color: var(--stone);
  }
  .membership {
    display: flex;
    align-items: center;
    gap: 5px;
    margin-top: 12px;
    font-size: 7px;
    font-weight: 500;
    letter-spacing: 0.1em;
    color: var(--stone);
    text-transform: uppercase;
  }
  .membership-badge {
    width: 9px;
    height: 9px;
    border-radius: 50%;
    background: var(--silver);
  }
</style>
</head>
<body>
  <main class="page">
    <div class="hero-photo" role="img" aria-label="Photograph of a white private jet fuselage, wing and engine against an overcast grey sky"></div>

    <header class="site-header">
      <div class="brand">
        <div class="brand-name">Halvern</div>
        <div>Aviation Group</div>
      </div>
      <nav class="main-nav">
        <span>Aircraft Management</span>
        <span>Aircraft Sales</span>
        <span>Pilot Services</span>
        <span>Flight Training</span>
        <svg class="menu-icon" width="12" height="8" viewBox="0 0 12 8" aria-hidden="true">
          <line x1="0" y1="1" x2="12" y2="1" stroke="#6b6a68" stroke-width="0.8"/>
          <line x1="3" y1="4" x2="12" y2="4" stroke="#6b6a68" stroke-width="0.8"/>
          <line x1="0" y1="7" x2="12" y2="7" stroke="#6b6a68" stroke-width="0.8"/>
        </svg>
      </nav>
    </header>

    <section class="hero-content">
      <p class="kicker">Our website is under construction and we will be</p>
      <h1 class="headline">Coming Soon</h1>
      <p class="launch-label">Launching In:</p>
      <div class="countdown">
        <div class="countdown-tile">175 d</div>
        <div class="countdown-tile">23 h</div>
        <div class="countdown-tile">46 m</div>
        <div class="countdown-tile">58 s</div>
      </div>
      <div class="membership">
        <span class="membership-badge"></span>
        <span>Member PQTR</span>
      </div>
    </section>
  </main>
</body>
</html>
```